varnity.com car care product labeling with cut outs will be printed on holographic sheet.

Need to make label for eco-friendly car care products. no hazard signs.
clean and simple design minimalism
wheel cleaner
tire shiner
glass cleaner
all purpose cleaner
247x90mm
166x150mm

Target Market(s)

eco friendly car care products. europe , uae

Industry/Entity Type

car care products, eco-friendly product line

Requirements
Must have
• BW design print on holographic sheet/label .eco-friendly signs
Nice to have
• premium product look and simplicity will be at first place, can be with cut outs

```html
<!DOCTYPE html>
<html lang="en">
<head>
<meta charset="utf-8">
<title>varnity car care labels</title>
<link href="https://fonts.googleapis.com/css2?family=Montserrat:wght@500;600;800&family=Roboto:wght@400&display=swap" rel="stylesheet">
<style>
  :root {
    --stage: #a6a6a6;
    --ink: #141414;
    --white: #f6f6f6;
    --all-purpose: #86b537;
    --tire: #7262a8;
    --glass: #65b1dc;
    --wheel: #d8ad3f;
    --badge: #5f9a3a;
  }
  * { box-sizing: border-box; margin: 0; padding: 0; }
  html, body { width: 1200px; height: 667px; overflow: hidden; }
  body {
    background: var(--stage);
    position: relative;
    font-family: 'Montserrat', sans-serif;
  }
  .caption {
    position: absolute;
    top: 43px;
    left: 0;
    width: 1147px;
    text-align: center;
    font-family: 'Roboto', sans-serif;
    font-size: 25px;
    color: var(--ink);
  }
  .label {
    position: absolute;
    top: 257px;
    width: 133px;
    height: 363px;
    overflow: hidden;
  }
  .label--all-purpose { left: 255px; --band: var(--all-purpose); }
  .label--tire { left: 432px; --band: var(--tire); }
  .label--glass { left: 617px; --band: var(--glass); }
  .label--wheel { left: 805px; --band: var(--wheel); }

  .holo {
    position: absolute;
    inset: 0 0 79px 0;
    background:
      linear-gradient(160deg, rgba(255,190,230,.55) 0%, rgba(255,255,255,0) 35%),
      linear-gradient(115deg,
        #c9e889 0%, #c89ed8 12%, #f3b9d6 22%, #9fd7b0 32%,
        #b5a1e2 42%, #eed49a 52%, #9ccfe0 62%, #d6a3dc 72%,
        #bfe39c 82%, #c7a9e6 92%, #f0c2d0 100%);
  }
  .mark-vertical {
    position: absolute;
    left: -8px;
    top: 282px;
    transform: rotate(-90deg);
    transform-origin: left top;
    font-size: 78px;
    font-weight: 600;
    line-height: 1;
    color: var(--white);
    white-space: nowrap;
    letter-spacing: -1px;
  }
  .brand {
    position: absolute;
    top: 16px;
    left: 0;
    right: 0;
    text-align: center;
    font-size: 25px;
    font-weight: 600;
    color: var(--ink);
    letter-spacing: -0.5px;
  }
  .product {
    position: absolute;
    top: 127px;
    left: 0;
    right: 0;
    text-align: center;
    font-size: 17px;
    font-weight: 800;
    line-height: 18px;
    color: var(--ink);
  }
  .label--all-purpose .product { font-size: 14px; line-height: 14px; top: 131px; }
  .product-rule {
    position: absolute;
    top: 166px;
    left: 16px;
    right: 0;
    height: 3px;
    background: var(--band);
  }
  .eco-badge {
    position: absolute;
    top: 213px;
    left: 71px;
    width: 44px;
    height: 44px;
    border-radius: 50%;
    background: var(--badge);
    opacity: .85;
  }
  .band {
    position: absolute;
    left: 0;
    right: 0;
    bottom: 0;
    height: 79px;
    background: var(--band);
  }
  .icons {
    position: absolute;
    top: 20px;
    left: 0;
    right: 0;
    display: flex;
    justify-content: center;
    align-items: center;
    gap: 5px;
  }
  .divider { width: 1px; height: 12px; background: var(--white); }
  .volume {
    position: absolute;
    bottom: 8px;
    left: 0;
    right: 0;
    text-align: center;
    font-size: 7px;
    font-weight: 600;
    color: var(--white);
  }
</style>
</head>
<body>
  <p class="caption">Printing with UV inks + white</p>

  <div class="label label--all-purpose">
    <div class="holo" role="img" aria-label="Holographic rainbow foil sheet"></div>
    <span class="mark-vertical">varnity</span>
    <span class="brand">varnity</span>
    <p class="product">ALL PURPOSE<br>CLEANER</p>
    <div class="product-rule"></div>
    <div class="eco-badge" aria-label="Eco friendly badge"></div>
    <div class="band">
      <div class="icons">
        <svg width="44" height="16" viewBox="0 0 44 16"><path d="M2 11 L4 7 L12 6 L17 2 L29 2 L35 6 L41 7 L42 11 Z" fill="#f6f6f6"/><circle cx="11" cy="12" r="3" fill="#f6f6f6" stroke="var(--all-purpose)" stroke-width="1.2"/><circle cx="33" cy="12" r="3" fill="#f6f6f6" stroke="var(--all-purpose)" stroke-width="1.2"/></svg>
      </div>
      <p class="volume">500 ml</p>
    </div>
  </div>

  <div class="label label--tire">
    <div class="holo" role="img" aria-label="Holographic rainbow foil sheet"></div>
    <span class="mark-vertical">varnity</span>
    <span class="brand">varnity</span>
    <p class="product">TIRE<br>SHINER</p>
    <div class="product-rule"></div>
    <div class="eco-badge" aria-label="Eco friendly badge"></div>
    <div class="band">
      <div class="icons">
        <svg width="44" height="16" viewBox="0 0 44 16"><path d="M2 11 L4 7 L12 6 L17 2 L29 2 L35 6 L41 7 L42 11 Z" fill="#f6f6f6"/><circle cx="11" cy="12" r="3" fill="#f6f6f6" stroke="var(--tire)" stroke-width="1.2"/><circle cx="33" cy="12" r="3" fill="#f6f6f6" stroke="var(--tire)" stroke-width="1.2"/></svg>
        <span class="divider"></span>
        <svg width="16" height="16" viewBox="0 0 16 16"><circle cx="8" cy="8" r="7" fill="none" stroke="#f6f6f6" stroke-width="1.4"/><circle cx="8" cy="8" r="3.5" fill="none" stroke="#f6f6f6" stroke-width="1.2"/></svg>
      </div>
      <p class="volume">500 ml</p>
    </div>
  </div>

  <div class="label label--glass">
    <div class="holo" role="img" aria-label="Holographic rainbow foil sheet"></div>
    <span class="mark-vertical">varnity</span>
    <span class="brand">varnity</span>
    <p class="product">GLASS<br>CLEANER</p>
    <div class="product-rule"></div>
    <div class="eco-badge" aria-label="Eco friendly badge"></div>
    <div class="band">
      <div class="icons">
        <svg width="44" height="16" viewBox="0 0 44 16"><path d="M2 11 L4 7 L12 6 L17 2 L29 2 L35 6 L41 7 L42 11 Z" fill="#f6f6f6"/><circle cx="11" cy="12" r="3" fill="#f6f6f6" stroke="var(--glass)" stroke-width="1.2"/><circle cx="33" cy="12" r="3" fill="#f6f6f6" stroke="var(--glass)" stroke-width="1.2"/></svg>
        <span class="divider"></span>
        <svg width="26" height="12" viewBox="0 0 26 12"><path d="M1 11 L6 2 L20 2 L25 11 Z" fill="none" stroke="#f6f6f6" stroke-width="1.3"/></svg>
      </div>
      <p class="volume">500 ml</p>
    </div>
  </div>

  <div class="label label--wheel">
    <div class="holo" role="img" aria-label="Holographic rainbow foil sheet"></div>
    <span class="mark-vertical">varnity</span>
    <span class="brand">varnity</span>
    <p class="product">WHEEL<br>CLEANER</p>
    <div class="product-rule"></div>
    <div class="eco-badge" aria-label="Eco friendly badge"></div>
    <div class="band">
      <div class="icons">
        <svg width="44" height="16" viewBox="0 0 44 16"><path d="M2 11 L4 7 L12 6 L17 2 L29 2 L35 6 L41 7 L42 11 Z" fill="#f6f6f6"/><circle cx="11" cy="12" r="3" fill="#f6f6f6" stroke="var(--wheel)" stroke-width="1.2"/><circle cx="33" cy="12" r="3" fill="#f6f6f6" stroke="var(--wheel)" stroke-width="1.2"/></svg>
        <span class="divider"></span>
        <svg width="16" height="16" viewBox="0 0 16 16"><circle cx="8" cy="8" r="7" fill="none" stroke="#f6f6f6" stroke-width="1.4"/><circle cx="8" cy="8" r="3.5" fill="none" stroke="#f6f6f6" stroke-width="1.2"/></svg>
      </div>
      <p class="volume">500 ml</p>
    </div>
  </div>
</body>
</html>
```